Web Design Project for lawn care business

after having a logo designed now my website is letting me down.
My websites main purpose is once i have made contact with a customer most will then try to research my company and the work i have done. Going to my unprofessional and untidy site will only put off potential customers. Also some customers will find my site online so must be able to grab their attention.

My site must be in keeping with my logo. Which is modern, sleek and classy. It needs to convey how professional we are and that the customer is getting a professional service.

My existing site will be replaced with the winning design.

Content wise and amount of pages will be similar to mine how ever more data will be inputted by myself.

so far prefer sites designed incorporating links in pictures or animated links to flick through pictures etc

breaks up the site and is more user friendly. 

also need to make sure colours are in keeping with logo or at least have similarities to keep it all uniform.

thanks

Industry/Entity Type

Lawn Care

Requirements
Nice to have
• in keeping font wise with my logo
same colours etc

```html
<!DOCTYPE html>
<html lang="en">
<head>
<meta charset="utf-8">
<title>Fairmow Lawn Care</title>
<link rel="stylesheet" href="https://fonts.googleapis.com/css2?family=Arimo:wght@400;700&display=swap">
<style>
  :root {
    --page-black: #070807;
    --shell: #1d1d1d;
    --shell-light: #2f2f2f;
    --panel: #020202;
    --lime-top: #e4f06a;
    --lime: #c3d62a;
    --lime-deep: #93a414;
    --accent: #d9e63c;
    --ink: #000000;
    --body-text: #c9c9c9;
    --photo-green: #4f8f2a;
  }
  * { box-sizing: border-box; margin: 0; padding: 0; }
  html, body { width: 1200px; height: 900px; overflow: hidden; }
  body {
    position: relative;
    font-family: "Arimo", Arial, sans-serif;
    background:
      linear-gradient(90deg, #1a2a0c 0, #0a0f06 28px, var(--page-black) 28px, var(--page-black) 1152px, #0a0f06 1152px, #1c2c0d 1200px);
  }
  .shell {
    position: absolute; left: 28px; top: 0; width: 1124px; height: 900px;
    background: linear-gradient(180deg, #232323 0, var(--shell) 120px, #171717 900px);
  }
  .abs { position: absolute; }

  /* header */
  .brand {
    left: 87px; top: 35px; width: 272px; height: 164px;
    background: #000; display: flex; align-items: center; justify-content: center; gap: 10px;
  }
  .brand-dot { width: 22px; height: 22px; border-radius: 50%; background: var(--lime); }
  .brand-name { color: var(--lime); font-weight: 400; font-size: 25px; letter-spacing: 0.5px; }
  .nav-band {
    left: 363px; top: 26px; width: 789px; height: 75px;
    background: linear-gradient(180deg, var(--lime-top) 0, var(--lime) 45%, var(--lime-deep) 100%);
    border-top-left-radius: 60px 75px;
  }
  .nav { left: 467px; top: 52px; display: flex; gap: 0; }
  .nav a { position: absolute; top: 0; color: var(--ink); text-decoration: none; font-weight: 700; font-size: 19px; white-space: nowrap; }
  .under-nav { left: 363px; top: 101px; width: 789px; height: 28px; background: #151515; }
  .sub-band { left: 381px; top: 129px; width: 771px; height: 70px; background: var(--shell-light); border-top-left-radius: 14px; }

  /* panels */
  .panel { background: var(--panel); border-radius: 16px; overflow: hidden; }
  .tab {
    height: 41px; display: flex; align-items: center; justify-content: center;
    background: linear-gradient(180deg, var(--lime-top) 0, var(--lime) 50%, var(--lime-deep) 100%);
    border-radius: 16px 16px 0 0; color: var(--ink); font-weight: 700; font-size: 23px;
  }
  .photo { position: absolute; }

  .sidebar { left: 52px; top: 234px; width: 292px; height: 700px; }
  .side-head {
    position: absolute; left: 35px; width: 222px;
    color: var(--accent); font-weight: 700; font-size: 16px;
    padding-bottom: 4px; border-bottom: 1px dotted #8a8a5a;
  }
  .side-note { position: absolute; left: 35px; width: 220px; color: var(--body-text); font-size: 14px; line-height: 21px; }

  .welcome { left: 416px; top: 234px; width: 700px; height: 379px; }
  .welcome .tab { font-size: 24px; letter-spacing: 0.5px; }
  .intro {
    position: absolute; left: 34px; top: 250px; width: 630px;
    color: var(--body-text); font-size: 14px; line-height: 21px;
  }
  .services { left: 416px; top: 648px; width: 700px; height: 300px; }
</style>
</head>
<body>
  <div class="shell"></div>

  <div class="abs brand"><span class="brand-dot"></span><span class="brand-name">Fairmow Lawn Care</span></div>

  <div class="abs nav-band"></div>
  <nav class="abs nav">
    <a href="#" style="left:0">Home</a>
    <a href="#" style="left:89px">Services</a>
    <a href="#" style="left:200px">Gallery</a>
    <a href="#" style="left:298px">About</a>
    <a href="#" style="left:386px">Contact</a>
  </nav>
  <div class="abs under-nav"></div>
  <div class="abs sub-band"></div>

  <aside class="abs panel sidebar">
    <div class="tab">Outdoor Maintenance</div>
    <div class="side-head" style="top:89px">Backyard maintenance</div>
    <div class="photo" role="img" aria-label="Landscaped backyard with stone steps, flower beds and lawn"
         style="left:35px; top:111px; width:252px; height:207px; background:linear-gradient(160deg,#8fbf4a,#3f7a22 55%,#7fae3a);"></div>
    <p class="side-note" style="top:327px">Make your backyard a paradise and a place of relaxation</p>
    <div class="side-head" style="top:398px">Front lawn maintenance</div>
    <div class="photo" role="img" aria-label="Striped front lawn bordered by flowering shrubs and trees"
         style="left:35px; top:419px; width:244px; height:186px; background:linear-gradient(180deg,#cfe2c8 0,#4d8a2c 30%,#5fa52a 60%,#3f8a1e);"></div>
    <p class="side-note" style="top:604px">Make your front lown welcoming to your friends and family.</p>
  </aside>

  <section class="abs panel welcome">
    <div class="tab">WELCOME TO FAIRMOW</div>
    <div class="photo" role="img" aria-label="Curving flower border of pink and yellow blooms beside a lawn"
         style="left:34px; top:77px; width:203px; height:154px; background:linear-gradient(120deg,#3f8a26,#d6457a 45%,#e0b23a 65%,#2f6e1e);"></div>
    <div class="photo" role="img" aria-label="House entrance with a gravel garden bed and shrubs"
         style="left:240px; top:80px; width:197px; height:151px; background:linear-gradient(180deg,#a9cde8 0,#c8a58a 35%,#9a8f7a 65%,#5f8a3a);"></div>
    <div class="photo" role="img" aria-label="Bed of red and yellow tulips edged with stone beside a lawn"
         style="left:441px; top:80px; width:222px; height:151px; background:linear-gradient(180deg,#7fb04a 0,#d94a2a 50%,#e8c83a 70%,#5c9a2a);"></div>
    <p class="intro">Fairmow is a proffesional lawn care and landscaping company.This website provides you with a source information related to lawn care,gardening,landscaping and a provider in proffectional assistance in other lawn care services.Your yard requires a regular care and maintainance with constant attention.In this website you will find information about our services that we offer.</p>
  </section>

  <section class="abs panel services">
    <div class="tab">Quality services</div>
    <div class="photo" role="img" aria-label="Close view of a red lawn mower on fresh grass"
         style="left:34px; top:79px; width:213px; height:152px; background:linear-gradient(90deg,#c8c8c8 0,#c0302a 35%,#7fb84a 60%,#4f8f2a);"></div>
    <div class="photo" role="img" aria-label="Worker driving a ride-on mower across a lawn"
         style="left:251px; top:79px; width:214px; height:152px; background:linear-gradient(180deg,#6fa23a 0,#8cbf4a 50%,#c03a2a 75%,#5a9a2a);"></div>
    <div class="photo" role="img" aria-label="Collage of grass, flowers, a mower and leafy plants"
         style="left:469px; top:79px; width:194px; height:152px; background:linear-gradient(135deg,#5fa0e0 0,#6fb03a 35%,#d8c83a 55%,#c0302a 75%,#4f8f2a);"></div>
  </section>
</body>
</html>
```